Financial Consulting Company in need of technical diagram

Attached is a basic template to follow, however the following changes must be made:
- Get rid of reflection boxes at the bottom
-Delete anything in parentheses
-Change top box to read "Uncover Value Opportunities"
-Change bottom right box to read "Sales and Operations Planning"
-Change bottom left box to read "Financial Planning"

Additionally we would like to see something a little more creative and cohesive. One possibility is using "Cheveron" type arrows to show the "wheel" effect.

Please email mtorvek@halbrine.example if you have any questions!
Updates

Please see newly uploaded image for an example of how we would like it re-created.

Project Deadline Extended

Industry/Entity Type

Financial

Requirements
Must have
• I'm looking for something that keeps the "wheel" approach, but is not a direct re-creation of the example given. The boxes for example, dont' necessarily need to stay boxes. Feel free to play around with placement as well.
Nice to have
• Please see green wheel for example of how it can be re-created.

```html
<!DOCTYPE html>
<html lang="en">
<head>
<meta charset="utf-8">
<title>Process Wheel</title>
<link rel="stylesheet" href="https://fonts.googleapis.com/css2?family=Source+Sans+3:wght@700;800;900&display=swap">
<style>
  :root {
    --bg: #ffffff;
    --glow: #b8f0ff;
    --ring-dark: #1a2fb8;
    --ring-mid: #2f63e0;
    --field-light: #5cc8f2;
    --field-deep: #2b5ee0;
    --arrow-fill: #ffffff;
    --label: #1f2fd6;
    --button-deep: #0a1f9a;
    --button-light: #4aa6f0;
    --title: #ffffff;
  }
  html, body {
    margin: 0;
    padding: 0;
    width: 1200px;
    height: 1200px;
    overflow: hidden;
    background: var(--bg);
  }
  .process-wheel {
    display: block;
    width: 1200px;
    height: 1200px;
  }
  .step-label {
    font-family: "Source Sans 3", sans-serif;
    font-weight: 900;
    fill: var(--label);
    text-anchor: middle;
  }
  .step-label .small { font-size: 26px; font-weight: 800; }
  .step-label .large { font-size: 50px; }
  .step-label .mid { font-size: 34px; }
  .process-title {
    font-family: "Source Sans 3", sans-serif;
    font-weight: 800;
    font-size: 58px;
    fill: var(--title);
    text-anchor: middle;
  }
</style>
</head>
<body>
<svg class="process-wheel" viewBox="0 0 1200 1200" xmlns="http://www.w3.org/2000/svg" aria-labelledby="wheel-title">
  <title id="wheel-title">Five-step process wheel</title>
  <defs>
    <radialGradient id="halo" cx="50%" cy="50%" r="50%">
      <stop offset="80%" stop-color="var(--glow)" stop-opacity="1"/>
      <stop offset="100%" stop-color="var(--glow)" stop-opacity="0"/>
    </radialGradient>
    <linearGradient id="ring" x1="0" y1="1" x2="1" y2="0">
      <stop offset="0" stop-color="var(--ring-mid)"/>
      <stop offset="1" stop-color="var(--ring-dark)"/>
    </linearGradient>
    <linearGradient id="field" x1="0" y1="1" x2="1" y2="0">
      <stop offset="0" stop-color="var(--field-light)"/>
      <stop offset="1" stop-color="var(--field-deep)"/>
    </linearGradient>
    <radialGradient id="button" cx="65%" cy="72%" r="75%">
      <stop offset="0" stop-color="var(--button-light)"/>
      <stop offset="0.55" stop-color="#1f4fd0"/>
      <stop offset="1" stop-color="var(--button-deep)"/>
    </radialGradient>
    <linearGradient id="rim" x1="0" y1="0" x2="1" y2="1">
      <stop offset="0" stop-color="#2a60e6"/>
      <stop offset="1" stop-color="#7cd4ff"/>
    </linearGradient>
    <path id="chevron" d="M1007 365 A470 470 0 0 1 1022.4 806 L888.8 809.8 L820.2 707.4 A245 245 0 0 0 812.2 477.5 L935.5 477.9 Z"/>
  </defs>

  <circle class="halo" cx="600" cy="600" r="600" fill="url(#halo)"/>
  <circle class="outer-ring" cx="600" cy="600" r="550" fill="url(#ring)"/>
  <circle class="wheel-field" cx="600" cy="600" r="508" fill="url(#field)"/>

  <g class="chevrons" fill="var(--arrow-fill)">
    <use href="#chevron" transform="rotate(-85 600 600)"/>
    <use href="#chevron" transform="rotate(-13 600 600)"/>
    <use href="#chevron" transform="rotate(59 600 600)"/>
    <use href="#chevron" transform="rotate(131 600 600)"/>
    <use href="#chevron" transform="rotate(203 600 600)"/>
  </g>

  <g class="step-label" transform="translate(612 245) rotate(4)">
    <text y="-20" class="large">UNCOVER</text>
    <text y="22" class="mid">VALUE</text>
    <text y="60" class="small">OPPORTUNITIES</text>
  </g>
  <g class="step-label" transform="translate(940 515) rotate(78)">
    <text y="-18" class="large">STRATEGIZE</text>
    <text y="20" class="small">and ALIGN</text>
  </g>
  <g class="step-label" transform="translate(800 880) rotate(-31)">
    <text y="-30" class="large">SALES &amp;</text>
    <text y="0" class="small">OPERATIONS</text>
    <text y="46" class="large">PLANNING</text>
  </g>
  <g class="step-label" transform="translate(382 870) rotate(40)">
    <text y="-14" class="mid">FINANCIAL</text>
    <text y="34" class="large">PLANNING</text>
  </g>
  <g class="step-label" transform="translate(275 478) rotate(-68)">
    <text y="-12" class="large">ASSESS</text>
    <text y="24" class="mid"><tspan class="small">the </tspan>RESULTS</text>
  </g>

  <circle class="hub-rim" cx="600" cy="600" r="245" fill="url(#rim)"/>
  <circle class="hub-edge" cx="600" cy="600" r="222" fill="#0c1f80"/>
  <circle class="hub-button" cx="600" cy="600" r="214" fill="url(#button)"/>
  <text class="process-title" x="600" y="575">PROCESS</text>
  <text class="process-title" x="600" y="655">TITLE</text>
</svg>
</body>
</html>
```